Banner & also another minor digital image for an Online Academic Journal

A direct example of what I need can be found in this webpage: http://papers.tbhu-archive.org/qrvt/
(Please see attached files, "sAMPLE", and "sAMPLE 2", so you can see what I mean.)
This link (http://papers.tbhu-archive.org/qrvt/) is for an existing ONLINE ACADEMIC JOURNAL at the Thornbury Hill University.
It will help for you to be acquainted with the format of Online Academic Journals.
You will find that there is a banner on top as well as a digital image of a journal/book cover on the right.
I need a
(1) banner and
a (2) digital journal/book cover
for a website for an ONLINE ACADEMIC JOURNAL.
I am looking for a serious, professional, elegant design.
There will not be a print version. Only web-based online publication. No coding needed, only PSD, JPG/PNG and PDF.
1) We use PelloWave (http://archives.pellowave.com/repository-software/journals/) for the digital image of the journal/book cover layout. Link shows the general layout of the journal website.
2) For the digital image of the journal/book cover and also the banner,
Name of the journal is....
"Lumen: A Quarterly of Civic Ethics and Recovery Work"
Only this text will be used and applied to both banner and cover.
***The color associated with the theme of dignity is purple
****You could also add the color red.
*****I don't want the design to be garish, but accents in red might represent
the sexual exploitation and violence in the title.
3) Attached "sAmple 2" file is a basic design for the digital image of the journal/book cover from PelloWave. I am looking for something more elegant and professional looking. Your creativity is encouraged. I am open to receiving your interpretation.
Target Market(s)
Academics & Community Professionals
Industry/Entity Type
Non Profit
Contact Information for Business Card
Match journal design

```html
<!DOCTYPE html>
<html lang="en">
<head>
<meta charset="utf-8">
<title>Lumen: A Quarterly of Civic Ethics and Recovery Work — Journal Cover</title>
<link rel="stylesheet" href="https://fonts.googleapis.com/css2?family=Raleway:wght@300;400;700&display=swap">
<style>
  :root {
    --page-bg: #ffffff;
    --ink-light: #ffffff;
    --plum-deep: #241a2e;
    --plum-dark: #3a2a47;
    --plum-mid: #6c5282;
    --plum-glow: #9c80b6;
    --panel-top: #5d4870;
    --panel-bottom: #9b82ae;
    --band: #9b81ad;
  }
  * { margin: 0; padding: 0; box-sizing: border-box; }
  html, body {
    width: 1200px;
    height: 1000px;
    overflow: hidden;
    background: var(--page-bg);
    font-family: "Raleway", sans-serif;
  }
  .canvas {
    position: relative;
    width: 1200px;
    height: 1000px;
  }
  .cover-art {
    position: absolute;
    left: 0;
    top: 0;
  }
  .contact {
    position: absolute;
    right: 274px;
    top: 36px;
    text-align: right;
    color: var(--ink-light);
    font-size: 17px;
    font-weight: 400;
    line-height: 26px;
  }
  .journal-title {
    position: absolute;
    left: 312px;
    top: 606px;
    color: var(--ink-light);
  }
  .journal-title .name {
    display: block;
    font-size: 52px;
    font-weight: 700;
    line-height: 58px;
    letter-spacing: 0.5px;
  }
  .journal-title .subtitle {
    display: block;
    font-size: 43px;
    font-weight: 300;
    line-height: 48px;
  }
  .editor-band {
    position: absolute;
    left: 287px;
    top: 927px;
    width: 657px;
    height: 65px;
    background: var(--band);
    color: var(--ink-light);
    font-size: 26px;
    font-weight: 400;
    display: flex;
    align-items: center;
    justify-content: center;
  }
</style>
</head>
<body>
  <main class="canvas">
    <svg class="cover-art" width="1200" height="1000" viewBox="0 0 1200 1000" aria-hidden="false">
      <defs>
        <linearGradient id="cover-base" x1="0" y1="0" x2="0.6" y2="1">
          <stop offset="0" stop-color="var(--plum-deep)"/>
          <stop offset="0.6" stop-color="var(--plum-mid)"/>
          <stop offset="1" stop-color="#7a5c96"/>
        </linearGradient>
        <radialGradient id="cover-glow" cx="620" cy="470" r="330" gradientUnits="userSpaceOnUse">
          <stop offset="0" stop-color="var(--plum-glow)" stop-opacity="0.95"/>
          <stop offset="1" stop-color="var(--plum-glow)" stop-opacity="0"/>
        </radialGradient>
        <linearGradient id="lower-panel" x1="0" y1="0" x2="0" y2="1">
          <stop offset="0" stop-color="var(--panel-top)"/>
          <stop offset="1" stop-color="var(--panel-bottom)"/>
        </linearGradient>
      </defs>
      <g class="cover-upper" role="img" aria-label="Soft purple gradient field with a subtle dotted texture">
        <rect x="287" y="5" width="657" height="912" fill="url(#cover-base)"/>
        <rect x="287" y="5" width="657" height="912" fill="url(#cover-glow)"/>
        <polygon class="corner-facet" points="510,5 944,5 944,395" fill="var(--plum-dark)" opacity="0.75"/>
      </g>
      <polygon class="lower-panel" points="287,418 944,607 944,917 287,917" fill="url(#lower-panel)"/>
    </svg>

    <div class="contact">
      <div>m.ashcombe@thornburyhill.edu</div>
      <div>www.archives.pellowave.com</div>
    </div>

    <h1 class="journal-title">
      <span class="name">LUMEN:</span>
      <span class="subtitle">A Quarterly of Civic Ethics</span>
      <span class="subtitle">and Recovery Work</span>
    </h1>

    <div class="editor-band">Marian L. Ashcombe, Editor-in-Chief</div>
  </main>
</body>
</html>
```